Plakate für Podologie - Medizinische Fusspflege
Zielgruppe
Podologie - Medizinische Fusspflege. Zielgruppe sind Kinder bis und mit ältere Menschen.
Aufgabenstellung
Möchte ein modernes, aber auch klassisches Design, dass Professionalität & medizinische Fundiertheit ausstrahlt. Man soll sehen, dass es medizinisch ist und nicht verwechselbar mit kosmetischer Fusspflege.

```html
<!DOCTYPE html>
<html lang="de">
<head>
<meta charset="utf-8">
<title>PediVita – Medizinische Podologie Plakat</title>
<link href="https://fonts.googleapis.com/css2?family=Barlow+Condensed:wght@500;600&family=Barlow:wght@400;500;600&display=swap" rel="stylesheet">
<style>
  :root{
    --teal-dark:#15675d;
    --teal:#1e7f72;
    --green:#6cb84b;
    --green-light:#86c664;
    --text-grey:#55595a;
    --bg:#e7e8ea;
    --white:#ffffff;
  }
  *{margin:0;padding:0;box-sizing:border-box}
  html,body{width:749px;height:1200px;overflow:hidden;background:var(--bg)}
  .poster{position:absolute;left:0;top:69px;width:749px;height:1061px;background:var(--white);overflow:hidden;font-family:'Barlow',sans-serif}
  .poster-shapes{position:absolute;inset:0;width:749px;height:1061px}
  .brand{position:absolute;left:54px;top:52px}
  .brand-mark{position:absolute;left:0;top:21px;width:60px;height:60px;border-radius:50%;background:var(--teal)}
  .brand-name{position:absolute;left:79px;top:30px;font-size:48px;font-weight:500;color:var(--teal-dark);white-space:nowrap;line-height:1}
  .brand-sub{position:absolute;left:80px;top:85px;font-size:12px;letter-spacing:2.2px;color:var(--text-grey);white-space:nowrap}
  .headline{position:absolute;left:40px;top:206px;font-family:'Barlow Condensed',sans-serif;font-weight:600;font-size:104px;line-height:86px;color:var(--teal-dark);letter-spacing:-1px}
  .headline span{display:block}
  .intro{position:absolute;left:44px;top:465px;font-size:19px;line-height:23px;color:var(--text-grey)}
  .intro-rule{position:absolute;left:44px;top:530px;width:124px;height:2px;background:var(--green)}
  .benefits{position:absolute;left:50px;top:543px;list-style:none}
  .benefits li{display:flex;align-items:center;height:53px;font-size:17.5px;font-weight:500;color:var(--teal-dark);letter-spacing:.3px}
  .benefits svg{width:32px;height:32px;margin-right:9px;flex:none}
  .cta{position:absolute;left:537px;top:659px;width:198px;height:198px;border-radius:50%;background:linear-gradient(135deg,var(--teal-dark),var(--teal));border:5px solid var(--green);display:flex;flex-direction:column;align-items:center;justify-content:center;font-family:'Barlow Condensed',sans-serif;font-weight:600;color:var(--white);line-height:.95;text-align:center}
  .cta .cta-top,.cta .cta-bottom{font-size:37px}
  .cta .cta-main{font-size:50px;color:var(--green-light)}
  .tagline{position:absolute;left:0;right:0;top:866px;text-align:center;font-family:'Barlow Condensed',sans-serif;font-weight:500;font-size:21px;color:var(--white)}
  .cert-badge{position:absolute;left:185px;top:910px;width:64px;height:64px;border-radius:50%;border:2px solid var(--green)}
  .cert-title{position:absolute;left:266px;top:915px;font-family:'Barlow Condensed',sans-serif;font-weight:500;font-size:29px;line-height:1;color:var(--white)}
  .cert-sub{position:absolute;left:266px;top:948px;font-family:'Barlow Condensed',sans-serif;font-weight:500;font-size:21px;line-height:1;color:var(--green-light)}
  .contact{position:absolute;left:0;right:0;top:1006px;text-align:center;font-size:16px;font-weight:600;color:var(--white);letter-spacing:.4px;white-space:nowrap}
  .contact .sep{color:var(--green);margin:0 13px}
</style>
</head>
<body>
<div class="poster">
  <svg class="poster-shapes" viewBox="0 0 1018 1442" preserveAspectRatio="none">
    <defs>
      <linearGradient id="photoTone" x1="0" y1="0" x2="0" y2="1">
        <stop offset="0" stop-color="#ecc9bb"/>
        <stop offset=".6" stop-color="#e2c0b2"/>
        <stop offset="1" stop-color="#d3e6c8"/>
      </linearGradient>
      <linearGradient id="photoFade" x1="0" y1="0" x2="1" y2="0">
        <stop offset="0" stop-color="#fff" stop-opacity="0"/>
        <stop offset=".35" stop-color="#fff" stop-opacity="1"/>
      </linearGradient>
      <mask id="photoMask">
        <rect x="600" y="150" width="418" height="950" fill="url(#photoFade)"/>
      </mask>
      <linearGradient id="bandTone" x1="0" y1="0" x2="1" y2="0">
        <stop offset="0" stop-color="#15675d"/>
        <stop offset="1" stop-color="#218a7b"/>
      </linearGradient>
    </defs>
    <path class="swoosh-green" d="M830 0 L960 0 C880 150 800 300 770 480 C740 700 780 900 830 1100 L730 1100 C680 880 660 650 700 430 C730 260 780 120 830 0 Z" fill="#7cbf5a"/>
    <path class="swoosh-line" d="M1000 0 L930 340" stroke="#1e7f72" stroke-width="10" fill="none"/>
    <rect class="photo-area" role="img" aria-label="Foto: Hände in grünen Handschuhen untersuchen eine Fusssohle" x="600" y="150" width="418" height="950" fill="url(#photoTone)" mask="url(#photoMask)"/>
    <path class="band" d="M0 1098 Q500 1072 1018 1082 L1018 1442 L0 1442 Z" fill="url(#bandTone)"/>
    <path class="band-edge" d="M0 1096 Q500 1066 1018 1074" stroke="#6cb84b" stroke-width="9" fill="none"/>
  </svg>

  <div class="brand">
    <div class="brand-mark"></div>
    <div class="brand-name">PediVita</div>
    <div class="brand-sub">MEDIZINISCHE PODOLOGIE</div>
  </div>

  <h1 class="headline"><span>IHRE FÜSSE.</span><span>UNSERE</span><span>KOMPETENZ.</span></h1>

  <p class="intro">Medizinische Fussbehandlungen<br>für Ihre Gesundheit und Lebensqualität.</p>
  <div class="intro-rule"></div>

  <ul class="benefits">
    <li><svg viewBox="0 0 34 34"><circle cx="17" cy="17" r="15.5" fill="none" stroke="#1e7f72" stroke-width="2"/><path d="M10 17.5l5 5 9-10" fill="none" stroke="#6cb84b" stroke-width="3.4" stroke-linecap="round" stroke-linejoin="round"/></svg>Nagel- &amp; Hautprobleme</li>
    <li><svg viewBox="0 0 34 34"><circle cx="17" cy="17" r="15.5" fill="none" stroke="#1e7f72" stroke-width="2"/><path d="M10 17.5l5 5 9-10" fill="none" stroke="#6cb84b" stroke-width="3.4" stroke-linecap="round" stroke-linejoin="round"/></svg>Hornhaut &amp; Hühneraugen</li>
    <li><svg viewBox="0 0 34 34"><circle cx="17" cy="17" r="15.5" fill="none" stroke="#1e7f72" stroke-width="2"/><path d="M10 17.5l5 5 9-10" fill="none" stroke="#6cb84b" stroke-width="3.4" stroke-linecap="round" stroke-linejoin="round"/></svg>Eingewachsene Nägel</li>
    <li><svg viewBox="0 0 34 34"><circle cx="17" cy="17" r="15.5" fill="none" stroke="#1e7f72" stroke-width="2"/><path d="M10 17.5l5 5 9-10" fill="none" stroke="#6cb84b" stroke-width="3.4" stroke-linecap="round" stroke-linejoin="round"/></svg>Diabetische Fußbehandlung</li>
    <li><svg viewBox="0 0 34 34"><circle cx="17" cy="17" r="15.5" fill="none" stroke="#1e7f72" stroke-width="2"/><path d="M10 17.5l5 5 9-10" fill="none" stroke="#6cb84b" stroke-width="3.4" stroke-linecap="round" stroke-linejoin="round"/></svg>Alle Kassen &amp; Privat</li>
  </ul>

  <div class="cta">
    <span class="cta-top">JETZT</span>
    <span class="cta-main">TERMIN</span>
    <span class="cta-bottom">SICHERN!</span>
  </div>

  <p class="tagline">AUCH FÜR RISIKOPATIENTEN, KINDER UND SPORTLER</p>
  <div class="cert-badge"></div>
  <p class="cert-title">ZERTIFIZIERTE PODOLOGEN</p>
  <p class="cert-sub">FACHGERECHT – HYGIENISCH – MODERN</p>

  <p class="contact">0123 / 456 789 0<span class="sep">|</span>pedivita.de<span class="sep">|</span>Musterstraße 1 12345 Musterstadt</p>
</div>
</body>
</html>
```